Food delivery wordpress design

need food delivery wordpress design for my site, here's the requirements
1. site must be pixel perfect , clean and professional
2. logo provided and must be match with the color scheme
3. pages : home , about us , faq , vendor registration

*** this is a information site no order can be made from the site, the site will show how things work , how to register as vendor , how to use the app , you may use any stock photo from lumbrevault and send me the code, i will purchase it

you may use any of the logo to play with it

***** It must look scale and not looks like template where I can purchase elsewhere
Updates

the designer told me he can't work as he got his personal problem, please check his message

Target Market(s)

those who prefer to purchase online

Font styles to use
Sans Serif

Requirements
Must have
• refer to zolvique.com/my
Nice to have
• everything user and vendor like to know

```html
<!DOCTYPE html>
<html lang="en">
<head>
<meta charset="utf-8">
<title>sizzlebox — food delivery</title>
<link href="https://fonts.googleapis.com/css2?family=Ubuntu:wght@400;500;700&family=Roboto:wght@400;500&display=swap" rel="stylesheet">
<style>
:root{
  --orange:#f9b233;
  --orange-deep:#f5a51c;
  --ink:#222222;
  --body:#444444;
  --muted:#6b6b6b;
  --dark-disc:#3a3a3a;
  --paper:#ffffff;
  --mist:#efefef;
  --line:#e2e2e2;
}
*{box-sizing:border-box;margin:0;padding:0}
html,body{width:1200px;height:3272px;overflow:hidden}
body{position:relative;background:var(--paper);font-family:'Roboto',Arial,sans-serif;color:var(--ink)}
.abs{position:absolute}
.heading{font-family:'Ubuntu',Arial,sans-serif;font-weight:500;color:var(--ink)}
.brand{font-family:'Ubuntu',Arial,sans-serif;font-weight:500;color:#3a3a3a;display:flex;align-items:center;gap:12px}
.brand .dot{width:44px;height:44px;border-radius:50%;background:var(--orange-deep)}
.mark-dot{border-radius:50%;background:var(--orange-deep)}

.header-bg{left:0;top:0;width:1200px;height:640px}
.nav a{position:absolute;white-space:nowrap;text-decoration:none;color:#3a3a3a;font-size:15px}
.pill-btn{border:2px solid #2b2b2b;border-radius:20px;background:var(--paper);font-family:'Ubuntu',Arial,sans-serif;color:#2b2b2b;display:flex;align-items:center;justify-content:center;gap:10px;box-shadow:2px 3px 0 rgba(0,0,0,.15)}
.pill-btn .mark-dot{width:22px;height:22px}

.hero-frame{left:137px;top:128px;width:926px;height:530px;background:var(--paper);box-shadow:0 10px 18px rgba(0,0,0,.08)}
.hero-photo{left:147px;top:138px;width:907px;height:510px;
  background:
    radial-gradient(ellipse 120px 90px at 38% 62%,rgba(214,40,30,.9),rgba(214,40,30,0) 70%),
    radial-gradient(ellipse 230px 170px at 66% 28%,rgba(238,222,196,.95),rgba(238,222,196,0) 70%),
    radial-gradient(ellipse 260px 170px at 70% 58%,rgba(236,196,70,.9),rgba(200,120,40,.5) 45%,rgba(0,0,0,0) 72%),
    radial-gradient(ellipse 380px 140px at 40% 92%,rgba(92,58,34,.95),rgba(92,58,34,0) 75%),
    linear-gradient(135deg,#2b2a2b 0,#1b1a1c 45%,#242220 100%);}
.tag{background:var(--orange);color:#2b2b2b;font-family:'Ubuntu',Arial,sans-serif;font-weight:500;padding:1px 8px 1px 6px;clip-path:polygon(0 0,100% 0,92% 100%,0 100%)}
.store-badge{background:#111;border:1.5px solid #c8c8c8;border-radius:6px;display:flex;align-items:center;gap:8px;padding:0 10px;color:#fff;font-family:'Roboto',Arial,sans-serif}
.store-badge .sym{flex:0 0 auto;border-radius:50%;background:#fff}
.store-badge .txt{display:flex;flex-direction:column;line-height:1}
.store-badge small{font-size:7px;text-transform:uppercase;letter-spacing:.3px}
.store-badge b{font-weight:500;font-size:17px;margin-top:2px}
.store-badge.sm{padding:0 6px;gap:5px;border-radius:4px}
.store-badge.sm small{font-size:4.5px}
.store-badge.sm b{font-size:10px;margin-top:1px}
.hero-dots span{position:absolute;left:0;width:10px;height:10px;border-radius:50%;background:var(--orange)}

.section-title{text-align:center;width:1200px;left:0}
.step-label{width:220px;text-align:center}
.step-label h3{font-family:'Roboto',Arial,sans-serif;font-weight:500;font-size:15px;color:var(--ink);margin-bottom:8px}
.step-label p{font-size:11.5px;line-height:17px;color:#333}
.food-photo{border-radius:50%;background:radial-gradient(circle,#b9783d 0,#d8a46c 40%,rgba(255,255,255,0) 70%)}

.mist{left:0;top:1295px;width:1200px;height:1823px;background:var(--mist)}
.about-text{font-size:12px;line-height:18px;color:var(--body)}
.feature{left:248px;width:350px;display:flex;gap:16px}
.feature .blob{flex:0 0 60px;height:60px;border-radius:50%;background:var(--orange);display:flex;align-items:center;justify-content:center}
.feature h4{font-size:14px;font-weight:500;color:var(--ink);margin:2px 0 6px}
.feature p{font-size:12px;line-height:18px;color:var(--body)}
.tablet{left:817px;top:1401px;width:240px;height:364px;border:2px solid #d6d6d6;border-radius:14px;background:var(--paper);box-shadow:0 4px 10px rgba(0,0,0,.1)}
.tablet-screen{left:826px;top:1431px;width:222px;height:301px;background:linear-gradient(180deg,#fff6e6,#fde2ac)}

.faq-item{height:41px;background:var(--paper);border:1px solid var(--line);font-family:'Ubuntu',Arial,sans-serif;font-size:16px;color:var(--orange-deep);display:flex;align-items:center;padding-left:18px}
.faq-item .toggle{position:absolute;right:-1px;top:-1px;width:41px;height:41px;background:var(--orange);color:#fff;font-size:20px;display:flex;align-items:center;justify-content:center;font-family:'Roboto',Arial,sans-serif}
.faq-open{background:var(--paper);border:1px solid var(--line)}
.faq-open p{font-size:11.5px;line-height:18px;color:var(--body);padding:16px 22px}

.form-card{left:218px;top:2556px;width:348px;height:477px;background:var(--paper)}
.form-head{left:226px;top:2565px;width:331px;height:45px;background:var(--orange);font-family:'Ubuntu',Arial,sans-serif;font-size:21px;color:#2b2b2b;display:flex;align-items:center;justify-content:center}
.field{left:243px;width:299px;height:33px;border:1px solid #d4d4d4;border-radius:3px;background:var(--paper);font-size:11.5px;color:#333;padding:9px 14px}

.contact-row{left:617px;display:flex;gap:20px;font-size:11.5px;line-height:18px;color:var(--body)}
.contact-row .ic{flex:0 0 32px;height:32px;border-radius:50%;background:var(--orange);display:flex;align-items:center;justify-content:center}

.footer-nav{font-size:14px;color:#333}
.social{width:32px;height:32px;border-radius:50%;display:flex;align-items:center;justify-content:center}
</style>
</head>
<body>

<svg class="abs header-bg" viewBox="0 0 1200 640" width="1200" height="640">
  <path d="M0 0H1200V500Q600 700 0 500Z" fill="#f9b233"/>
  <path d="M0 500Q600 700 1200 500" fill="none" stroke="#ffffff" stroke-width="5"/>
  <path d="M0 508Q600 708 1200 508" fill="none" stroke="#f5a51c" stroke-width="3"/>
</svg>

<div class="abs brand" style="left:174px;top:32px;font-size:44px">
  <span class="dot"></span><span>sizzlebox<span style="font-size:16px;margin-left:4px">.com</span></span>
</div>

<nav class="abs nav" style="left:0;top:0">
  <a style="left:546px;top:62px">Home</a>
  <a style="left:623px;top:62px">About Us</a>
  <a style="left:724px;top:62px">FAQ</a>
</nav>
<div class="abs pill-btn" style="left:797px;top:51px;width:223px;height:35px;font-size:16px"><span class="mark-dot"></span>Vendor registration</div>

<div class="abs hero-frame"></div>
<div class="abs hero-photo" role="img" aria-label="Photograph of a sliced chicken and vegetable wrap on a wooden board with cherry tomatoes and corn"></div>
<div class="abs tag" style="left:222px;top:276px;font-size:12px">Welcome to</div>
<div class="abs heading" style="left:220px;top:288px;font-size:48px;color:#fff;font-weight:500">sizzlebox</div>
<div class="abs heading" style="left:446px;top:336px;font-size:22px;color:#fff;font-weight:400">.com</div>
<div class="abs store-badge" style="left:229px;top:387px;width:134px;height:40px"><span class="sym" style="width:18px;height:18px"></span><span class="txt"><small>Get it on</small><b>Play Shelf</b></span></div>
<div class="abs store-badge" style="left:371px;top:387px;width:134px;height:40px"><span class="sym" style="width:18px;height:18px"></span><span class="txt"><small>Download on the</small><b>App Shelf</b></span></div>
<div class="abs hero-dots" style="left:177px;top:380px">
  <span style="top:0"></span><span style="top:23px;background:#fff"></span><span style="top:46px"></span><span style="top:69px"></span>
</div>

<div class="abs food-photo" style="left:-40px;top:660px;width:250px;height:250px" role="img" aria-label="Photograph of grilled chicken skewers with herbs"></div>
<div class="abs food-photo" style="left:970px;top:1020px;width:260px;height:240px" role="img" aria-label="Photograph of grilled chicken skewers with herbs"></div>

<div class="abs mark-dot" style="left:574px;top:722px;width:54px;height:54px"></div>
<h2 class="abs heading section-title" style="top:782px;font-size:36px;font-weight:500">how it works</h2>

<svg class="abs" style="left:0;top:870px" width="1200" height="200" viewBox="0 870 1200 200">
  <g stroke="#e3e3e3" stroke-width="4" stroke-linecap="round">
    <line x1="222" y1="906" x2="258" y2="906"/><line x1="198" y1="920" x2="252" y2="920"/><line x1="212" y1="934" x2="232" y2="934"/>
    <line x1="470" y1="901" x2="498" y2="901"/><line x1="442" y1="915" x2="490" y2="915"/>
    <line x1="703" y1="901" x2="731" y2="901"/><line x1="675" y1="915" x2="723" y2="915"/>
  </g>
  <g fill="none" stroke="#f9b233" stroke-width="2">
    <path d="M442 952H462M454 944L462 952L454 960"/>
    <path d="M676 952H696M688 944L696 952L688 960"/>
    <path d="M916 952H936M928 944L936 952L928 960"/>
  </g>
  <g>
    <circle cx="356" cy="965" r="85" fill="none" stroke="#f9b233" stroke-width="3"/>
    <circle cx="356" cy="965" r="76" fill="none" stroke="#cfcfcf" stroke-width="1.5" stroke-dasharray="4 3"/>
    <circle cx="356" cy="965" r="71" fill="#3a3a3a"/>
    <circle cx="590" cy="965" r="85" fill="none" stroke="#f9b233" stroke-width="3"/>
    <circle cx="590" cy="965" r="76" fill="none" stroke="#cfcfcf" stroke-width="1.5" stroke-dasharray="4 3"/>
    <circle cx="590" cy="965" r="71" fill="#3a3a3a"/>
    <circle cx="829" cy="965" r="85" fill="none" stroke="#f9b233" stroke-width="3"/>
    <circle cx="829" cy="965" r="76" fill="none" stroke="#cfcfcf" stroke-width="1.5" stroke-dasharray="4 3"/>
    <circle cx="829" cy="965" r="71" fill="#3a3a3a"/>
  </g>
  <g fill="none" stroke="#fff" stroke-width="2" stroke-linecap="round">
    <path d="M338 968A24 18 0 0 1 386 968Z"/><line x1="334" y1="975" x2="390" y2="975"/><path d="M338 982H386"/>
    <line x1="326" y1="960" x2="334" y2="960"/><line x1="324" y1="968" x2="334" y2="968"/><line x1="326" y1="976" x2="332" y2="976"/>
    <rect x="575" y="935" width="30" height="60" rx="4"/><path d="M582 958A8 8 0 0 1 598 958Z"/><circle cx="590" cy="976" r="6"/><path d="M587 976l2 2 4-4"/>
    <rect x="810" y="942" width="26" height="46" rx="3"/><rect x="822" y="955" width="34" height="24" rx="3"/><line x1="816" y1="984" x2="826" y2="984"/>
  </g>
  <text x="838" y="972" font-family="Roboto,Arial,sans-serif" font-size="9" fill="#fff" font-weight="500">PAY</text>
  <g font-family="Ubuntu,Arial,sans-serif" font-size="24" fill="#fff">
    <circle cx="286" cy="924" r="20" fill="#f9b233" stroke="#fff" stroke-width="3"/><text x="286" y="933" text-anchor="middle">01</text>
    <circle cx="524" cy="924" r="20" fill="#f9b233" stroke="#fff" stroke-width="3"/><text x="524" y="933" text-anchor="middle">02</text>
    <circle cx="764" cy="924" r="20" fill="#f9b233" stroke="#fff" stroke-width="3"/><text x="764" y="933" text-anchor="middle">03</text>
  </g>
</svg>

<div class="abs step-label" style="left:246px;top:1067px"><h3>Lorium ipsum</h3><p>Quisque id sollicitudin nulla.<br>Morbi eget pretium sapien</p></div>
<div class="abs step-label" style="left:480px;top:1067px"><h3>Lorium ipsum</h3><p>Phasellus scelerisque<br>convallis risus.</p></div>
<div class="abs step-label" style="left:719px;top:1067px"><h3>Lorium ipsum</h3><p>Quisque id sollicitudin nulla.<br>Morbi eget pretium sapien</p></div>

<div class="abs pill-btn" style="left:489px;top:1181px;width:222px;height:33px;font-size:16px;letter-spacing:.5px"><span class="mark-dot"></span>REGISTER NOW</div>

<div class="abs mist"></div>

<div class="abs mark-dot" style="left:180px;top:1360px;width:58px;height:58px"></div>
<div class="abs tag" style="left:256px;top:1362px;font-size:12px">About Us</div>
<h2 class="abs heading" style="left:256px;top:1376px;font-size:35px;font-weight:500">how to use the app</h2>
<p class="abs about-text" style="left:258px;top:1420px;width:375px">Proin ornare posuere quam ut euismod. Nam eu nunc vitae orci ultrices imperdiet ut id ligula. Sed interdum eros eget sagittis rutrum. Vestibulum in elementum mauris. In iaculis odio urna.</p>

<div class="abs feature" style="top:1502px">
  <div class="blob"><svg width="26" height="26" viewBox="0 0 26 26" fill="none" stroke="#fff" stroke-width="1.8"><path d="M13 4V17M8 12L13 17L18 12M5 21H21"/></svg></div>
  <div><h4>Download the app</h4><p>Proin ornare posuere quam ut euismod. Nam eu nunc vitae orci ultrices imperdiet ut id ligula.</p></div>
</div>
<div class="abs feature" style="top:1585px">
  <div class="blob"><svg width="26" height="26" viewBox="0 0 26 26" fill="none" stroke="#fff" stroke-width="1.8"><path d="M8 4V22M5 4V10Q8 13 11 10V4M18 22V4Q22 8 21 14H18"/></svg></div>
  <div><h4>Lorium ipsum dolor amit</h4><p>Proin ornare posuere quam ut euismod. Nam eu nunc vitae orci ultrices imperdiet ut id ligula.</p></div>
</div>
<div class="abs feature" style="top:1670px">
  <div class="blob"><svg width="26" height="26" viewBox="0 0 26 26" fill="none" stroke="#fff" stroke-width="1.8"><circle cx="13" cy="9" r="5"/><path d="M4 23Q4 15 13 15Q22 15 22 23Z"/></svg></div>
  <div><h4>Vendor Registration</h4><p>Proin ornare posuere quam ut euismod. Nam eu nunc vitae orci ultrices imperdiet ut id ligula.</p></div>
</div>
<div class="abs store-badge" style="left:259px;top:1761px;width:133px;height:39px"><span class="sym" style="width:18px;height:18px"></span><span class="txt"><small>Get it on</small><b>Play Shelf</b></span></div>
<div class="abs store-badge" style="left:400px;top:1761px;width:132px;height:39px"><span class="sym" style="width:18px;height:18px"></span><span class="txt"><small>Download on the</small><b>App Shelf</b></span></div>

<div class="abs" style="left:675px;top:1385px;width:100px;height:330px;border-radius:40px;background:linear-gradient(180deg,#6f8a3e,#3f5a22)" role="img" aria-label="Photograph of a bundle of fresh rosemary tied with string"></div>
<div class="abs" style="left:600px;top:1705px;width:60px;height:70px;border-radius:50%;background:radial-gradient(circle,#f1e6ea,#d4c0c8)" role="img" aria-label="Photograph of a garlic clove and scattered peppercorns"></div>
<div class="abs" style="left:1116px;top:1460px;width:52px;height:245px;border-radius:26px 26px 8px 8px;background:linear-gradient(180deg,#f4f2ee 0,#d8b27a 22%,#c79a5c 100%)" role="img" aria-label="Photograph of a wooden spoon holding coarse salt"></div>

<div class="abs tablet"></div>
<div class="abs tablet-screen"></div>
<div class="abs mark-dot" style="left:907px;top:1470px;width:62px;height:62px"></div>
<div class="abs heading" style="left:826px;top:1566px;width:222px;text-align:center;font-size:30px;line-height:28px;color:#3a3a3a">sizzle<br>box<span style="font-size:13px;display:block;line-height:14px">.com</span></div>
<div class="abs pill-btn" style="left:853px;top:1660px;width:165px;height:25px;font-size:10px;border-width:1.5px"><span class="mark-dot" style="width:16px;height:16px"></span>DOWNLOAD ME FIRST</div>

<svg class="abs" style="left:0;top:1780px" width="1200" height="160" viewBox="0 1780 1200 160">
  <path d="M0 1796Q600 2026 1200 1796" fill="none" stroke="#ffffff" stroke-width="4"/>
  <path d="M0 1803Q600 2033 1200 1803" fill="none" stroke="#f9b233" stroke-width="5"/>
</svg>

<div class="abs mark-dot" style="left:573px;top:1966px;width:56px;height:56px"></div>
<h2 class="abs heading section-title" style="top:2027px;font-size:36px;font-weight:500">frequently asked questions</h2>

<div class="abs faq-open" style="left:222px;top:2112px;width:356px;height:110px">
  <div class="faq-item" style="position:relative;border:none;border-bottom:1px solid var(--line)">Lorium ipsum dolor amit ?<span class="toggle">&minus;</span></div>
  <p>Proin ornare posuere quam ut euismod. Nam eu nunc vitae orci ultrices imperdiet ut id ligula.</p>
</div>
<div class="abs faq-item" style="left:222px;top:2233px;width:356px">Lorium ipsum dolor amit ?<span class="toggle">+</span></div>
<div class="abs faq-item" style="left:222px;top:2286px;width:356px">Lorium ipsum dolor amit ?<span class="toggle">+</span></div>
<div class="abs faq-item" style="left:222px;top:2339px;width:356px">Lorium ipsum dolor amit ?<span class="toggle">+</span></div>

<div class="abs faq-item" style="left:621px;top:2112px;width:356px">Lorium ipsum dolor amit ?<span class="toggle">+</span></div>
<div class="abs faq-item" style="left:621px;top:2165px;width:356px">Lorium ipsum dolor amit ?<span class="toggle">+</span></div>
<div class="abs faq-item" style="left:621px;top:2218px;width:356px">Lorium ipsum dolor amit ?<span class="toggle">+</span></div>
<div class="abs faq-item" style="left:621px;top:2272px;width:356px">Lorium ipsum dolor amit ?<span class="toggle">+</span></div>
<div class="abs faq-item" style="left:621px;top:2325px;width:356px">Lorium ipsum dolor amit ?<span class="toggle">+</span></div>

<svg class="abs" style="left:0;top:2440px" width="1200" height="150" viewBox="0 2440 1200 150">
  <path d="M0 2578Q600 2336 1200 2578" fill="none" stroke="#f9b233" stroke-width="5"/>
  <path d="M0 2586Q600 2344 1200 2586" fill="none" stroke="#ffffff" stroke-width="3"/>
</svg>

<div class="abs form-card"></div>
<div class="abs form-head">vendor registration</div>
<p class="abs" style="left:240px;top:2628px;width:305px;text-align:center;font-size:11.5px;line-height:18px;color:var(--body)">Neque porro quisquam est qui dolorem ipsum quia dolor sit amet, consectetur, adipisci velit...</p>
<div class="abs field" style="top:2690px">First name*</div>
<div class="abs field" style="top:2735px">Last name*</div>
<div class="abs field" style="top:2781px">Vendor name</div>
<div class="abs field" style="top:2827px">Email*</div>
<div class="abs field" style="top:2873px">Phone</div>
<div class="abs field" style="top:2917px;height:70px">Message</div>
<div class="abs pill-btn" style="left:282px;top:3010px;width:222px;height:33px;font-size:17px;letter-spacing:.5px"><span class="mark-dot"></span>REGISTER NOW</div>

<h2 class="abs heading" style="left:611px;top:2578px;font-size:35px;font-weight:500;color:#3a3a3a">Contact Us</h2>
<p class="abs" style="left:614px;top:2640px;width:400px;font-size:11.5px;line-height:18px;color:var(--body)">Lorem ipsum dolor sit amet, consectetur adipiscing elit. Suspendisse eleifend libero metus, sit amet fermentum magna</p>

<div class="abs contact-row" style="top:2704px">
  <div class="ic"><svg width="16" height="16" viewBox="0 0 16 16"><path d="M8 1A5 5 0 0 0 3 6C3 10 8 15 8 15S13 10 13 6A5 5 0 0 0 8 1Z" fill="#3a3a3a"/><circle cx="8" cy="6" r="2" fill="#f9b233"/></svg></div>
  <div>level 2, wisma teratai 8 jalan<br>kenanga lima,<br>Kuala Lumpur-50480<br>Malaysia.</div>
</div>
<div class="abs contact-row" style="top:2780px">
  <div class="ic"><svg width="16" height="16" viewBox="0 0 16 16"><path d="M3 2L6 2L7 5L5 6.5Q6.5 9.5 9.5 11L11 9L14 10L14 13Q8 14 2 5Z" fill="#3a3a3a"/></svg></div>
  <div style="padding-top:7px">03 5550 1842</div>
</div>
<div class="abs contact-row" style="top:2826px">
  <div class="ic"><svg width="16" height="16" viewBox="0 0 16 16"><rect x="2" y="4" width="12" height="9" rx="1" fill="#3a3a3a"/><path d="M2.5 5L8 9L13.5 5" fill="none" stroke="#f9b233" stroke-width="1.2"/></svg></div>
  <div style="padding-top:7px">info@sizzlebox.com</div>
</div>
<div class="abs" style="left:617px;top:2883px;width:407px;height:146px;border:3px solid #fff;background:linear-gradient(160deg,#eef0ec,#e2e6e0 60%,#f3e3b4 80%,#e8eaf0)" role="img" aria-label="Street map showing the office location"></div>

<div class="abs" style="left:0;top:3118px;width:1200px;height:154px;background:var(--paper)"></div>
<div class="abs brand" style="left:216px;top:3150px;font-size:40px">
  <span class="dot" style="width:50px;height:50px"></span><span>sizzlebox<span style="font-size:15px;margin-left:4px">.com</span></span>
</div>
<div class="abs" style="left:220px;top:3225px;font-size:11.5px;color:#333">&copy; 2021 &nbsp;|&nbsp; www.sizzlebox.com</div>

<div class="abs footer-nav" style="left:795px;top:3167px">Home</div>
<div class="abs footer-nav" style="left:872px;top:3167px">About Us</div>
<div class="abs footer-nav" style="left:973px;top:3167px">FAQ</div>

<div class="abs store-badge sm" style="left:711px;top:3207px;width:84px;height:28px"><span class="sym" style="width:11px;height:11px"></span><span class="txt"><small>Get it on</small><b>Play Shelf</b></span></div>
<div class="abs store-badge sm" style="left:801px;top:3207px;width:83px;height:28px"><span class="sym" style="width:11px;height:11px"></span><span class="txt"><small>Download on the</small><b>App Shelf</b></span></div>
<div class="abs social" style="left:896px;top:3205px;border:1.5px solid #e3e3e3;background:#fff" aria-label="social link"></div>
<div class="abs social" style="left:934px;top:3205px;background:var(--orange)" aria-label="social link"></div>
<div class="abs social" style="left:972px;top:3205px;background:var(--orange)" aria-label="social link"></div>

</body>
</html>
```